German tourism publishing house needs for international wellness hotel guide

We are planning as a print catalog. For this hotel directory we need a meaningful and appealing cover. The contents, a wide offer of wellness hotels should be recognizable at first sight. The title should make you want to go on a wellness holiday. The target group of the book are customers. We are looking forward to your next visit! The title "Wellness Hotels" should be larger on the cover written. The "Bravora logo" should be smaller on the cover. Please integrate the Internet address www.bravora-example.de small on the cover

Industry/Entity Type

Tourism

Font styles to use
Serif
Sans Serif

Colors
0355a3
ffffff
85acd3

Requirements
Must have
• We are looking forward to your next visit! The title "Wellness Hotels" should be larger on the cover written. The "Bravora logo" should be smaller on the cover.
Nice to have
• Please integrate the Internet address www.bravora-example.de small on the cover

```html
<!DOCTYPE html>
<html lang="en">
<head>
<meta charset="utf-8">
<title>Wellness Hotels – Cover Spread</title>
<link rel="stylesheet" href="https://fonts.googleapis.com/css2?family=Cinzel:wght@400;500&family=Cormorant+Garamond:wght@500;600&family=EB+Garamond:wght@400&display=swap">
<style>
  :root {
    --brand-blue: #0355a3;
    --deep-blue: #1d5ea8;
    --soft-blue: #85acd3;
    --pale-blue: #dbe7f3;
    --white: #ffffff;
    --stage: #eeeeee;
  }
  * { box-sizing: border-box; margin: 0; padding: 0; }
  html, body { width: 1200px; height: 800px; overflow: hidden; background: var(--stage); }
  .spread {
    position: absolute; left: 200px; top: 115px;
    width: 800px; height: 570px; display: flex;
    box-shadow: 0 14px 40px rgba(0,0,0,.18);
  }
  /* Back cover */
  .back-cover {
    width: 380px; height: 100%; background: var(--white);
    position: relative; padding: 34px 28px 0; overflow: hidden;
  }
  .back-copy {
    position: relative; z-index: 1;
    font-family: "EB Garamond", serif; font-size: 9.6px; line-height: 1.38;
    color: var(--brand-blue); text-align: justify; hyphens: auto;
  }
  .back-copy p + p { margin-top: 12px; }
  .back-photo {
    position: absolute; left: 0; top: 320px; width: 380px; height: 250px;
  }
  .back-brand {
    position: absolute; left: 0; right: 0; top: 332px; text-align: center; z-index: 1;
  }
  /* Spine */
  .spine {
    width: 40px; height: 100%; background: var(--brand-blue);
    display: flex; flex-direction: column; align-items: center;
    padding: 30px 0 16px;
  }
  .spine-title {
    writing-mode: vertical-rl; font-family: "Cinzel", serif;
    color: var(--white); font-size: 22px; letter-spacing: 2px;
  }
  .spine-subtitle {
    writing-mode: vertical-rl; font-family: "Cinzel", serif;
    color: var(--soft-blue); font-size: 13px; letter-spacing: 6px; margin-top: 24px;
  }
  .spine-brand {
    writing-mode: vertical-rl; margin-top: auto;
    font-family: "Cormorant Garamond", serif; font-weight: 600;
    font-size: 11px; color: var(--white);
  }
  /* Front cover */
  .front-cover {
    width: 380px; height: 100%; position: relative; overflow: hidden;
    background: linear-gradient(180deg, var(--deep-blue) 0%, #4f86c2 14%, #a9c4e2 26%, var(--white) 36%, var(--white) 100%);
  }
  .cover-title {
    position: absolute; top: 72px; left: 0; right: 0; text-align: center;
    font-family: "Cinzel", serif; font-weight: 400; color: var(--white);
    font-size: 56px; letter-spacing: -1px; line-height: 1; z-index: 1;
  }
  .cover-title .initial { font-size: 78px; }
  .cover-subtitle {
    position: absolute; top: 150px; left: 0; right: 0; text-align: center;
    font-family: "Cinzel", serif; color: var(--brand-blue);
    font-size: 36px; letter-spacing: 14px; padding-left: 14px; line-height: 1; z-index: 1;
  }
  .cover-subtitle.reflection {
    top: 188px; transform: scaleY(-1); opacity: .18;
    -webkit-mask-image: linear-gradient(to top, #000 0%, transparent 70%);
    mask-image: linear-gradient(to top, #000 0%, transparent 70%);
  }
  .cover-photo { position: absolute; left: 0; top: 232px; width: 380px; height: 276px; }
  .brand-name {
    font-family: "Cormorant Garamond", serif; font-weight: 600;
    color: var(--brand-blue); font-size: 28px; line-height: 1;
  }
  .front-brand {
    position: absolute; top: 514px; left: 0; right: 0; text-align: center;
    display: flex; flex-direction: column; align-items: center; gap: 6px;
  }
  .front-brand .brand-name { font-size: 26px; }
  .cover-url {
    font-family: "EB Garamond", serif; font-size: 10px; letter-spacing: .5px;
    color: var(--brand-blue);
  }
</style>
</head>
<body>
<main class="spread">
  <section class="back-cover">
    <svg class="back-photo" viewBox="0 0 380 250" role="img" aria-label="Soft blue-tinted photo of a guest relaxing in a bright spa room">
      <defs>
        <radialGradient id="backPhotoGlow" cx=".68" cy=".5" r=".6">
          <stop offset="0" stop-color="#b9cfe7"/>
          <stop offset=".55" stop-color="#dbe7f3"/>
          <stop offset="1" stop-color="#ffffff"/>
        </radialGradient>
        <linearGradient id="backPhotoFade" x1="0" y1="0" x2="0" y2="1">
          <stop offset="0" stop-color="#ffffff" stop-opacity="1"/>
          <stop offset=".3" stop-color="#ffffff" stop-opacity="0"/>
          <stop offset=".8" stop-color="#ffffff" stop-opacity="0"/>
          <stop offset="1" stop-color="#ffffff" stop-opacity="1"/>
        </linearGradient>
      </defs>
      <rect width="380" height="250" fill="url(#backPhotoGlow)"/>
      <rect width="380" height="250" fill="url(#backPhotoFade)"/>
    </svg>
    <div class="back-copy">
      <p>Lorem ipsum dolor sit amet, consectetur adipiscing elit. Nullam feugiat neque in varius molestie. Pellentesque rhoncus scelerisque molestie. Nulla consectetur libero ut ex pharetra ultricies. Mauris id tempor augue. Suspendisse facilisis purus ac velit dictum gravida. Phasellus neque enim, fringilla sit amet mollis et, aliquet sed elit. Curabitur consectetur accumsan sem, in fringilla arcu euismod ut. Nunc eget euismod arcu. Nulla suscipit tempor mattis quis posuere. Nulla a lectus ac diam posuere venenatis. Nam faucibus pretium tincidunt. Nunc eu mi lectus. Nunc at turpis et nibh sodales malesuada. Nulla ipsum augue, blandit nec convallis ornare, consectetur a lacus. Proin vel feugiat risus.</p>
      <p>Pellentesque auctor libero ac turpis euismod viverra. Etiam aliquam vel nunc ut vehicula. Sed nec hendrerit lacus. Suspendisse interdum volutpat magna non dapibus. Morbi malesuada vehicula leo, ac malesuada felis ultrices laoreet. Cras ornare fermentum urna, sit amet dapibus tortor tristique in. Sed vitae ex ullamcorper, sodales est sit amet, vestibulum massa. Duis dapibus dolor sit amet neque gravida efficitur. Fusce vel volutpat felis. Nunc eget pretium urna, vitae accumsan leo. Ut quis ante bibendum, maximus nulla in, aliquet arcu. Aliquam et imperdiet ligula. Nullam blandit erat quis tellus vulputate feugiat. Donec non imperdiet urna. Praesent aliquam mattis odio, vel volutpat lacus egestas sit amet. Integer tristique ipsum vel mi accumsan convallis.</p>
    </div>
    <div class="back-brand"><span class="brand-name">Bravora</span></div>
  </section>

  <aside class="spine">
    <span class="spine-title">WELLNESS</span>
    <span class="spine-subtitle">HOTELS</span>
    <span class="spine-brand">Bravora</span>
  </aside>

  <section class="front-cover">
    <h1 class="cover-title"><span class="initial">W</span>ELLNESS</h1>
    <p class="cover-subtitle">HOTELS</p>
    <p class="cover-subtitle reflection" aria-hidden="true">HOTELS</p>
    <svg class="cover-photo" viewBox="0 0 380 276" role="img" aria-label="Blue-toned photo of a wellness hotel terrace with sun loungers, a canopy daybed, parasol and garden trees">
      <defs>
        <linearGradient id="frontPhotoTone" x1="0" y1="0" x2="0" y2="1">
          <stop offset="0" stop-color="#ffffff"/>
          <stop offset=".18" stop-color="#c6d8ec"/>
          <stop offset=".45" stop-color="#6f9bcd"/>
          <stop offset=".7" stop-color="#4a7fbf"/>
          <stop offset=".88" stop-color="#a9c4e2"/>
          <stop offset="1" stop-color="#ffffff"/>
        </linearGradient>
        <linearGradient id="frontPhotoSide" x1="0" y1="0" x2="1" y2="0">
          <stop offset="0" stop-color="#2f66ac" stop-opacity=".25"/>
          <stop offset=".5" stop-color="#ffffff" stop-opacity="0"/>
          <stop offset="1" stop-color="#2f66ac" stop-opacity=".2"/>
        </linearGradient>
      </defs>
      <rect width="380" height="276" fill="url(#frontPhotoTone)"/>
      <rect width="380" height="276" fill="url(#frontPhotoSide)"/>
    </svg>
    <div class="front-brand">
      <span class="brand-name">Bravora</span>
      <span class="cover-url">www.bravora-example.de</span>
    </div>
  </section>
</main>
</body>
</html>
```